Design for a creative video production company !!

Looking for a 3-4 page layout for my project proposals. Should include :
Cover page
Page 1: is the general overview (see attached)
Page 2: Project Outline ( a blank area to add project specifics)
Page 3: budget (a blank table here I can add in the numbers)

final version a pdf I can edit. even just a page design I can add as my background. More info on company please go to www.brightvalefilms.com

Target Market(s)

Marketing managers, communications people, people who want to use video ... professional video to tell their story or educate.

Industry/Entity Type

It Company

Font styles to use
Serif
Sans Serif

Colors

Designer to choose colors to be used in the design.

Requirements
Must have
• Must have a way I can fill in the information later, I'm happy to use a background and leave an area black I can add a table for budgets. Would like to see a pie chart or graph used to show the time of each stage of the project. See general overview doc attached.
Nice to have
• A variation of the proposal I attached is just a start, Please look at website, (brightvalefilms.com) business cards, and proposal as an idea of the branding.
Should not have
• sad clowns

```html
<!DOCTYPE html>
<html lang="en">
<head>
<meta charset="utf-8">
<title>Brightvale Films – Proposal Pages</title>
<link href="https://fonts.googleapis.com/css2?family=Lato:wght@400;700;900&display=swap" rel="stylesheet">
<style>
  :root {
    --red: #a01c2c;
    --red-bright: #d7263a;
    --ink: #2a2a2a;
    --grey-dark: #555;
    --grey-mid: #9a9a9a;
    --grey-light: #c4c4c4;
    --paper: #ffffff;
    --stage: #e4e4e4;
  }
  * { box-sizing: border-box; margin: 0; padding: 0; }
  html, body { width: 1200px; height: 1200px; overflow: hidden; }
  body { background: var(--stage); font-family: "Lato", sans-serif; color: var(--ink); position: relative; }

  .page { position: absolute; width: 500px; height: 386px; background: var(--paper); overflow: hidden;
          box-shadow: 0 3px 10px rgba(0,0,0,.25); }
  .page--overview { left: 80px; top: 174px; }
  .page--outline  { left: 649px; top: 174px; }
  .page--budget   { left: 373px; top: 614px;
                    background: radial-gradient(ellipse at 55% 35%, #fafafa 0%, #e9e9e9 60%, #dcdcdc 100%); }

  .band { position: absolute; background: var(--red); }
  .band--top { left: 0; top: 14px; height: 22px; width: 184px; clip-path: polygon(0 0, 88% 0, 100% 100%, 0 100%); }
  .band--bottom { right: 0; bottom: 20px; height: 22px; width: 152px; clip-path: polygon(12% 0, 100% 0, 100% 100%, 0 100%); }

  .wordmark { position: absolute; font-weight: 900; letter-spacing: .2px; text-transform: uppercase; white-space: nowrap; }
  .wordmark--dark { right: 12px; top: 16px; font-size: 15px; color: var(--ink); }
  .wordmark--faint { right: 32px; top: 20px; font-size: 16px; color: #b5b5b5; }

  /* overview page */
  .title-band { position: absolute; left: 0; top: 14px; width: 266px; height: 25px; background: var(--red);
                clip-path: polygon(0 0, 93% 0, 100% 100%, 0 100%); }
  .title-band h1 { color: #fff; font-size: 17px; font-weight: 700; line-height: 25px; padding-left: 12px; }
  .header-rule { position: absolute; left: 0; right: 0; top: 38px; height: 2px; background: var(--red); }
  .intro { position: absolute; left: 12px; right: 22px; top: 46px; font-size: 5.4px; line-height: 7.6px; color: #444; }

  .stage { position: absolute; width: 150px; }
  .stage__icon { position: absolute; left: -28px; top: 0; width: 18px; height: 18px; }
  .stage h2 { color: var(--red); font-size: 8.2px; font-weight: 700; line-height: 10px; margin-bottom: 8px; }
  .stage h3 { color: var(--red); font-size: 5px; font-weight: 400; }
  .stage p { font-size: 5px; line-height: 6.6px; color: #333; margin-bottom: 6px; text-align: justify; }
  .stage--collab { left: 35px; top: 88px; }
  .stage--preprod { left: 203px; top: 90px; }
  .stage--filming { left: 35px; top: 192px; }
  .stage--editing { left: 203px; top: 192px; }

  .timeline-chart { position: absolute; left: 360px; top: 106px; width: 130px; height: 150px; }

  .payment-title { position: absolute; left: 33px; top: 290px; color: var(--red); font-size: 8px; font-weight: 700; }
  .payment-band { position: absolute; left: 0; right: 0; top: 307px; height: 59px; background: var(--red); color: #fff;
                  font-size: 5.4px; line-height: 8px; }
  .payment-band .col-a { position: absolute; left: 32px; top: 5px; width: 220px; }
  .payment-band .col-b { position: absolute; left: 255px; top: 5px; width: 205px; font-size: 5.8px; line-height: 7.6px; }
  .payment-band ul { list-style: none; display: grid; grid-template-columns: 70px 110px; margin-top: 3px; }
  .payment-band li::before { content: "• "; }
  .payment-band strong { font-size: 8px; }

  /* outline page */
  .feature-image { position: absolute; left: 0; top: 50px; width: 340px; height: 336px;
                   background: radial-gradient(ellipse at 40% 55%, rgba(0,0,0,.09) 0%, rgba(0,0,0,.04) 45%, rgba(0,0,0,0) 75%); }

  /* budget page */
  .budget-table { position: absolute; left: 70px; top: 76px; width: 374px; height: 214px; display: flex;
                  border-radius: 14px; overflow: hidden; background: #fff;
                  box-shadow: 0 2px 6px rgba(0,0,0,.28); }
  .budget-col { display: flex; flex-direction: column; position: relative; }
  .budget-col--a { width: 110px; }
  .budget-col--b { width: 153px; background: linear-gradient(90deg,#f1f1f1,#fff 12%,#fff 88%,#f1f1f1); }
  .budget-col--c { width: 111px; }
  .budget-col__head { height: 40px; display: flex; align-items: center; justify-content: center;
                      font-size: 7px; font-weight: 700; color: #fff; background: var(--red); }
  .budget-col--b .budget-col__head { background: var(--grey-light); color: #555; font-weight: 400; }
  .budget-col__rows { padding: 32px 12px 0; display: flex; flex-direction: column; gap: 25px; }
  .budget-col__rows span { display: block; height: 1.2px; background: var(--red); }
  .budget-col--b .budget-col__rows { padding: 32px 33px 0; }
  .budget-col--b .budget-col__rows span { background: var(--grey-mid); }
  .site-url { position: absolute; left: 206px; top: 349px; font-size: 6.6px; letter-spacing: 1.6px; color: #333; }
</style>
</head>
<body>

<!-- Page 1: overview -->
<section class="page page--overview">
  <div class="title-band"><h1>Let’s tell your story together</h1></div>
  <div class="wordmark wordmark--dark">Brightvale Films</div>
  <div class="header-rule"></div>
  <p class="intro">At Brightvale Films, we take a creative, collaborative, planned approach to creating exceptional videos. We take you on a journey from start to finish, guiding you through the stages, and eliminating the element of surprise (other than the final reveal!).<br>Our goal is to give you the peace of mind that we will tell your vision and message. Here are the 4 stages that you can expect with a breakdown of the time usually required at each stage:</p>

  <div class="stage stage--collab">
    <svg class="stage__icon" viewBox="0 0 18 18"><rect x="3" y="2" width="12" height="15" rx="1" fill="none" stroke="#333" stroke-width="1.2"/><path d="M5.5 6h7M5.5 9h7M5.5 12h7" stroke="#333" stroke-width="1"/></svg>
    <h2>Collaboration +<br>Script development</h2>
    <h3>Brightvale Films’ role:</h3>
    <p>We seek to understand the CTA, the audience, your product/service and your brand. Armed with this understanding, we then work backwards, to develop and bring the script to life.</p>
    <h3>Your role:</h3>
    <p>Act as a collaborator to help us capture your idea, provide context, information and research to help us understand your story.</p>
  </div>

  <div class="stage stage--preprod">
    <svg class="stage__icon" viewBox="0 0 18 18"><path d="M4 8l10-4v3L4 11z" fill="#333"/><rect x="4" y="11" width="10" height="6" fill="none" stroke="#333" stroke-width="1.2"/></svg>
    <h2>Pre-production</h2>
    <h3>Brightvale Films’ role:</h3>
    <p>In preparation for the shoot, handle logistics (location, equipment rentals, crew, talent, other).</p>
    <h3>Your role:</h3>
    <p>As applicable, liaising with talent, organizing locations in conjunction with Brightvale Films, other.</p>
  </div>

  <div class="stage stage--filming">
    <svg class="stage__icon" viewBox="0 0 18 18"><rect x="8" y="4" width="8" height="5" fill="#333"/><path d="M12 9l-3 8M12 9l3 8M12 9v8" stroke="#333" stroke-width="1"/><circle cx="5" cy="5" r="2" fill="#333"/><path d="M5 7v6M5 13l-2 4M5 13l2 4M5 9h3" stroke="#333" stroke-width="1.4"/></svg>
    <h2>Filming</h2>
    <h3>Brightvale Films’ role:</h3>
    <p>directing and filming, managing all on-site parties, coaching talent, other.</p>
    <h3>Your role:</h3>
    <p>attend as needed to ensure messaging is on point. Also, a chance to be part of the action! Capture “behind the scenes” as needed.</p>
  </div>

  <div class="stage stage--editing">
    <svg class="stage__icon" viewBox="0 0 18 18"><rect x="2" y="4" width="14" height="10" fill="#333"/><path d="M7 6.5v5l4.5-2.5z" fill="#fff"/></svg>
    <h2>Editing</h2>
    <h3>Brightvale Films’ role:</h3>
    <p>Culling the raw footage into a compelling, concise finished product, in alignment with the final script. This is also when animation occurs (if applicable).</p>
    <h3>Your role:</h3>
    <p>There are 2 screenings included in the quote. All feedback is captured and addressed online.</p>
  </div>

  <svg class="timeline-chart" viewBox="0 0 130 150" font-family="Lato, sans-serif">
    <path d="M5 0V105H130" fill="none" stroke="#444" stroke-width=".6"/>
    <path d="M2 0h3M2 20h3M2 40h3M2 60h3M2 80h3" stroke="#444" stroke-width=".5"/>
    <rect x="20" y="65" width="10" height="40" fill="var(--red)"/>
    <rect x="52" y="90" width="10" height="15" fill="var(--grey-light)"/>
    <rect x="83" y="90" width="10" height="15" fill="var(--grey-dark)"/>
    <rect x="116" y="65" width="10" height="40" fill="var(--red-bright)"/>
    <g font-size="5" fill="#333" text-anchor="middle">
      <text x="25" y="62">40%</text><text x="57" y="87">15%</text>
      <text x="88" y="87">15%</text><text x="121" y="62">40%</text>
    </g>
    <g font-size="4.2" fill="#333">
      <rect x="18" y="118" width="3" height="3" fill="var(--red)"/><text x="25" y="121">Collaboration + Script development</text>
      <rect x="18" y="126" width="3" height="3" fill="var(--grey-light)"/><text x="25" y="129">Pre-production</text>
      <rect x="18" y="134" width="3" height="3" fill="var(--grey-dark)"/><text x="25" y="137">Filming</text>
      <rect x="18" y="142" width="3" height="3" fill="var(--red-bright)"/><text x="25" y="145">Editing</text>
    </g>
  </svg>

  <div class="payment-title">Payment process</div>
  <div class="payment-band">
    <div class="col-a">
      For projects under 30 days, payment is due upon project completion<br>
      For projects over 30 days, we invoice at the following milestones:
      <ul>
        <li>Upon script approval</li><li>Prior to pre-production</li>
        <li>Upon script approval</li><li>After 2 screenings</li>
      </ul>
    </div>
    <div class="col-b">If additional screenings are required, additional hours are <strong>$x.</strong><br>Upon receiving final payment, the watermark is removed from the final version.</div>
  </div>
</section>

<!-- Page 2: project outline -->
<section class="page page--outline">
  <div class="band band--top"></div>
  <div class="wordmark wordmark--faint">Brightvale Films</div>
  <div class="feature-image" role="img" aria-label="Faint greyscale photo of a cinema camera rig"></div>
  <div class="band band--bottom"></div>
</section>

<!-- Page 3: budget -->
<section class="page page--budget">
  <div class="band band--top"></div>
  <div class="wordmark wordmark--faint">Brightvale Films</div>
  <div class="budget-table">
    <div class="budget-col budget-col--a">
      <div class="budget-col__head">Lorem Ipsum</div>
      <div class="budget-col__rows"><span></span><span></span><span></span><span></span><span></span></div>
    </div>
    <div class="budget-col budget-col--b">
      <div class="budget-col__head">Lorem Ipsum</div>
      <div class="budget-col__rows"><span></span><span></span><span></span><span></span><span></span></div>
    </div>
    <div class="budget-col budget-col--c">
      <div class="budget-col__head">Lorem Ipsum</div>
      <div class="budget-col__rows"><span></span><span></span><span></span><span></span><span></span></div>
    </div>
  </div>
  <div class="site-url">www.brightvalefilms.com</div>
  <div class="band band--bottom"></div>
</section>

</body>
</html>
```